Stationery Design Project

Would like to have the design elements we created in for our website (www.brook-holdings.example), incorporated in a stationery design layout.
Updates
Colors used in the logo attachments do not need to be used. We are open to different color variations. Looking for a crisp, clean, modern update using the design elements in attachments and which can also be viewed on or website.
A note to designers:
Project Deadline Extended
Reason: Due to update in our project description and requirements, we have decided to extend the deadline of this project to provide ample opportunity to all designers participating .
Requirements
Must have
- Must have continuity with the theme and design features used in our website. Have attached .jpg images of some of the design elements.

```html
<!DOCTYPE html>
<html lang="en">
<head>
<meta charset="utf-8">
<title>Brook Holdings, Inc. — Letterhead</title>
<link rel="stylesheet" href="https://fonts.googleapis.com/css2?family=Source+Sans+3:wght@400;600&display=swap">
<style>
  :root {
    --paper: #ffffff;
    --brand-blue: #1e7fc0;
    --brand-green: #6abf3f;
    --band-gold: #bf9a3e;
    --band-text: #fdf8ee;
    --rule-grey: #6b6b6b;
    --sign-ink: #e9e9e9;
  }
  * { margin: 0; padding: 0; box-sizing: border-box; }
  html, body { width: 948px; height: 1200px; overflow: hidden; background: var(--paper); }
  .letterhead {
    position: relative;
    width: 948px;
    height: 1200px;
    background: var(--paper);
    font-family: "Source Sans 3", sans-serif;
  }
  .brand {
    position: absolute;
    top: 62px;
    left: 0;
    width: 100%;
    display: flex;
    justify-content: center;
    align-items: center;
    gap: 12px;
  }
  .brand-dot {
    width: 22px;
    height: 22px;
    border-radius: 50%;
    background: var(--brand-green);
  }
  .brand-name {
    font-size: 66px;
    font-weight: 400;
    color: var(--brand-blue);
    letter-spacing: -0.5px;
    line-height: 1;
  }
  .signature {
    position: absolute;
    left: 634px;
    top: 978px;
    width: 264px;
    height: 130px;
    background: linear-gradient(135deg, var(--sign-ink), #f7f7f7);
    border-radius: 4px;
  }
  .footer-rule {
    position: absolute;
    left: 0;
    top: 1130px;
    width: 100%;
    height: 2px;
    background: var(--rule-grey);
  }
  .contact-band {
    position: absolute;
    left: 0;
    top: 1138px;
    width: 100%;
    height: 62px;
    background: var(--band-gold);
    color: var(--band-text);
    text-align: center;
    font-size: 15px;
    padding-top: 8px;
    letter-spacing: 0.2px;
  }
  .contact-line {
    display: flex;
    justify-content: center;
    align-items: center;
    gap: 6px;
    height: 20px;
  }
  .contact-item { display: inline-flex; align-items: center; gap: 4px; margin-right: 6px; }
  .contact-item svg { width: 12px; height: 12px; fill: var(--band-text); }
  .address-line { margin-top: 6px; font-size: 15px; letter-spacing: 0.6px; }
</style>
</head>
<body>
  <main class="letterhead">
    <header class="brand">
      <span class="brand-dot"></span>
      <span class="brand-name">Brook Holdings, Inc.</span>
    </header>

    <div class="signature" role="img" aria-label="Handwritten signature with a drawn leaf"></div>

    <div class="footer-rule"></div>

    <footer class="contact-band">
      <div class="contact-line">
        <span class="contact-item">
          <svg viewBox="0 0 12 12" aria-hidden="true"><path d="M2.5 1l2 2.5-1 1.2a7 7 0 0 0 3.8 3.8l1.2-1 2.5 2-1 1.5C6 11 1 6 1 2.5z"/></svg>
          (555) 014-2290
        </span>
        <span class="contact-item">
          <svg viewBox="0 0 12 12" aria-hidden="true"><rect x="3" y="1" width="6" height="4"/><rect x="1" y="5" width="10" height="4" rx="1"/><rect x="3" y="8" width="6" height="3"/></svg>
          (555) 014-2291
        </span>
        <span class="contact-item">
          <svg viewBox="0 0 12 12" aria-hidden="true"><rect x="1" y="3" width="10" height="6" rx="1"/></svg>
          info@brook-holdings.example
        </span>
        <span class="contact-item">
          <svg viewBox="0 0 12 12" aria-hidden="true"><circle cx="6" cy="6" r="4.5"/></svg>
          www.brook-holdings.example
        </span>
      </div>
      <div class="address-line">418 Alder Lane Suite 12, Fairview, OR 97000</div>
    </footer>
  </main>
</body>
</html>
```